Motivationsplakat
Sehr schönes Design und sehr angenehme Zusammenarbeit. Ging umgehend auf meine Wünsche ein. Immer wieder gerne! Vielen Dank!
Zielgruppe
Wir, der SC Wendorf aus der Schweiz, sind ein Fussballverein welcher in der 4. höchsten Liga spielt. Der hier zu erstellende Banner (Fusszeile) ist vorwiegend für die Spieler der 1. Mannschaft, als 'Motivationsspritze' auf diversen Plakaten (z.B. auf A1 Plakat wo die Aufstellung draufgeschrieben wird), gedacht.
Aufgabenstellung
Der Banner (als Fussleiste eines Plakates oder als eigenständiger Banner benutzbar) sollte ein Verhältniss von 1 zu 4 haben (also z.B. 50 cm hoch und 200 cm breit). Auf dem Banner muss das Logo des SC Wendorf drauf sein (im Anhang). Dazu muss es folgende Texte enthalten:
- Saison 2017/18
- Die Leidenschaft und den Verein im Herzen!
Der Spruch sollte als zentrale Botschaft verstanden werden und durch die grafische Gestalltung verstärkt/unterstützt werden.
Im Anhang sende ich ihnen noch ein paar Fotos von Spielern, welche sie eventuell verwenden könnten (muss nicht sein). Es dürften jedoch keine Spielergesichter erkennbar sein, also nur z.B. das Dress.

```html
<!DOCTYPE html>
<html lang="de">
<head>
<meta charset="utf-8">
<title>SC Wendorf – Saison 2017/18</title>
<link href="https://fonts.googleapis.com/css2?family=Barlow:wght@600;700&display=swap" rel="stylesheet">
<style>
  :root {
    --bg: #000000;
    --red: #e30b17;
    --white: #ffffff;
    --grass: #2f5a14;
    --flame: #e2561a;
  }
  html, body {
    margin: 0;
    padding: 0;
    width: 1200px;
    height: 300px;
    overflow: hidden;
    background: var(--bg);
  }
  .banner {
    position: relative;
    width: 1200px;
    height: 300px;
    background: var(--bg);
    font-family: "Barlow", "Arial Narrow", sans-serif;
    overflow: hidden;
  }
  .banner__photo {
    position: absolute;
    left: 0;
    top: 0;
    width: 480px;
    height: 300px;
    background:
      radial-gradient(ellipse 55% 40% at 35% 65%, rgba(226, 86, 26, 0.75), rgba(226, 86, 26, 0) 70%),
      linear-gradient(to bottom, var(--bg) 0%, var(--bg) 55%, var(--grass) 100%);
  }
  .headline {
    position: absolute;
    left: 0;
    top: 16px;
    width: 1174px;
    margin: 0;
    color: var(--red);
    font-weight: 700;
    font-size: 57px;
    line-height: 59px;
    text-align: center;
    letter-spacing: 1px;
    text-transform: uppercase;
  }
  .season {
    position: absolute;
    left: 410px;
    top: 150px;
    width: 310px;
    margin: 0;
    color: var(--white);
    font-weight: 600;
    font-size: 41px;
    line-height: 48px;
    text-align: center;
    letter-spacing: 1px;
    text-transform: uppercase;
  }
  .club-name {
    position: absolute;
    left: 890px;
    top: 150px;
    width: 280px;
    margin: 0;
    color: var(--white);
    font-weight: 700;
    font-size: 46px;
    line-height: 56px;
    text-align: center;
    letter-spacing: 1px;
    text-transform: uppercase;
  }
</style>
</head>
<body>
  <main class="banner">
    <div class="banner__photo" role="img" aria-label="Foto: Bein eines Spielers in roten Stutzen kickt einen brennenden Fussball über den Rasen"></div>
    <h1 class="headline">Die Leidenschaft und den<br>Verein im Herzen!</h1>
    <p class="season">Saison 2017/18</p>
    <p class="club-name">SC Wendorf</p>
  </main>
</body>
</html>
```